Bref créative
Karvelo ApS wants a cool new identity on stationary
Total outline for the stationary stuff
Simple
Henrik Dahlquist
CEO
Birkeslette 218
5810 Naestved
Denmark
henrik@karvelo.dk
www.karvelo.dk
Free your mind
We want the design to show trust, technology, to be frontrunner, inovation etc. - streamlined with a crisp look.

```html
<!DOCTYPE html>
<html lang="en">
<head>
<meta charset="utf-8">
<title>Karvelo ApS – Stationery</title>
<link href="https://fonts.googleapis.com/css2?family=Open+Sans:wght@400;600;700&display=swap" rel="stylesheet">
<style>
:root{
  --bg:#d8d8d6;
  --paper:#ffffff;
  --green:#8dc63f;
  --dark:#3b3b3d;
  --ink:#4a4a4a;
  --muted:#9a9a9a;
  --faint:#ececec;
  --rule:#cfcfcf;
}
*{box-sizing:border-box;margin:0;padding:0}
html,body{width:1200px;height:727px;overflow:hidden;background:var(--bg);font-family:"Open Sans",Arial,sans-serif;color:var(--ink)}
.canvas{position:relative;width:1200px;height:727px;overflow:hidden;background:var(--bg)}
.item{position:absolute;background:var(--paper);box-shadow:0 2px 6px rgba(0,0,0,.18);overflow:hidden}

.brand{display:flex;align-items:center;gap:6px;font-weight:600;color:var(--dark);line-height:1}
.brand .mark{display:block;background:var(--green)}
.brand.sm{font-size:17px}.brand.sm .mark{width:14px;height:14px}
.brand.md{font-size:22px}.brand.md .mark{width:18px;height:18px}
.brand.light{color:#fff}

.tiny{font-size:5px;line-height:1.5;color:var(--muted)}
.faint-square{position:absolute;border:14px solid var(--faint)}

/* business cards */
.card-back{left:12px;top:40px;width:245px;height:68px}
.card-back .brand{position:absolute;left:14px;top:14px}
.card-back .tiny{position:absolute;right:14px;top:14px;text-align:right}
.card-front{left:12px;top:110px;width:245px;height:66px;display:flex}
.card-front .name-tab{width:92px;background:var(--dark);color:#fff;padding:20px 8px;font-size:9px;font-weight:600}
.card-front .name-tab small{display:block;font-size:6px;font-weight:400;color:#cfcfcf;margin-top:2px}
.card-front .contact{padding:16px 10px;border-top:3px solid var(--green);flex:1}
.card-green{left:269px;top:40px;width:235px;height:136px;background:var(--green)}
.card-dark{left:516px;top:40px;width:216px;height:136px;background:var(--dark)}
.card-white{left:744px;top:40px;width:235px;height:136px}
.card-center{position:absolute;left:50%;top:44%;transform:translate(-50%,-50%)}
.outline-square{width:34px;height:34px;border:5px solid #fff}
.card-url{position:absolute;left:0;right:0;bottom:16px;text-align:center;font-size:10px;letter-spacing:1px;font-weight:600}
.card-green .card-url{color:#fff}
.card-white .card-url{color:var(--muted)}

/* compliment sheet + envelope */
.sheet{left:12px;top:187px;width:408px;height:230px}
.sheet .brand{position:absolute;left:20px;top:18px}
.sheet .tiny{position:absolute;left:20px;top:46px}
.envelope{left:12px;top:402px;width:408px;height:300px}
.envelope svg{position:absolute;inset:0}
.envelope .brand{position:absolute;left:50%;top:64px;transform:translateX(-50%)}

/* letterhead */
.letter{left:432px;top:187px;width:360px;height:533px;padding:24px 26px}
.letter .head{display:flex;justify-content:space-between}
.letter .recipient{margin-top:40px}
.letter p{font-size:5.2px;line-height:1.6;color:var(--muted);margin-top:10px;max-width:250px}
.letter .greeting{margin-top:22px}
.signature{display:block;width:60px;height:20px;margin-top:18px;background:linear-gradient(90deg,#d4daf0,#eef0f8)}
.letter .faint-square{right:-30px;bottom:40px;width:150px;height:150px}

/* fax */
.fax{left:804px;top:187px;width:372px;height:533px;padding:24px 26px}
.fax .head{display:flex;justify-content:space-between}
.fax-title{text-align:right;font-size:20px;font-weight:400;color:var(--muted);margin-top:24px;letter-spacing:1px}
.fax-table{width:100%;border-collapse:collapse;margin-top:6px;font-size:5.5px;color:var(--ink)}
.fax-table td{border:1px solid var(--rule);height:15px;padding:0 4px}
.fax-table td.lbl{width:34px;background:#e4e4e4}
.checks{display:flex;gap:10px;margin-top:10px;font-size:5px;color:var(--muted)}
.checks span::before{content:"";display:inline-block;width:5px;height:5px;border:1px solid var(--muted);margin-right:3px;vertical-align:-1px}
.comments{margin-top:14px;font-size:5.5px;color:var(--ink)}
.fax .faint-square{right:-30px;bottom:40px;width:150px;height:150px}
</style>
</head>
<body>
<main class="canvas">

  <section class="item card-back">
    <div class="brand sm"><span class="mark"></span>Karvelo</div>
    <div class="tiny">Karvelo ApS<br>Birkeslette 218<br>5810 Naestved<br>Denmark</div>
  </section>

  <section class="item card-front">
    <div class="name-tab">Henrik Dahlquist<small>CEO</small></div>
    <div class="contact tiny">henrik@karvelo.dk<br>www.karvelo.dk<br>Birkeslette 218, 5810 Naestved</div>
  </section>

  <section class="item card-green">
    <div class="card-center outline-square"></div>
    <div class="card-url">www.karvelo.dk</div>
  </section>

  <section class="item card-dark">
    <div class="card-center outline-square"></div>
  </section>

  <section class="item card-white">
    <div class="card-center brand md"><span class="mark"></span>Karvelo</div>
    <div class="card-url">www.karvelo.dk</div>
  </section>

  <section class="item sheet">
    <div class="brand md"><span class="mark"></span>Karvelo</div>
    <div class="tiny">Birkeslette 218, 5810 Naestved, Denmark</div>
    <div class="faint-square" style="right:30px;top:30px;width:150px;height:150px"></div>
  </section>

  <section class="item envelope">
    <svg width="408" height="300" viewBox="0 0 408 300" aria-hidden="true">
      <polyline points="0,20 204,120 408,20" fill="none" stroke="#d0d0d0" stroke-width="1.5"/>
      <polygon points="0,170 204,245 408,170 408,300 0,300" fill="#3b3b3d"/>
    </svg>
    <div class="brand sm"><span class="mark"></span>Karvelo</div>
  </section>

  <section class="item letter">
    <div class="head">
      <div class="brand md"><span class="mark"></span>Karvelo</div>
      <div class="tiny" style="text-align:left">Karvelo ApS<br>Birkeslette 218<br>5810 Naestved<br>Denmark<br>www.karvelo.dk</div>
    </div>
    <div class="recipient tiny">Recipient Name<br>Sample Street 12<br>8000 Aarhus</div>
    <p class="greeting">Dear Recipient,</p>
    <p>We are pleased to present our new stationery. Every item shares one crisp, streamlined look built on trust and technology. Please let us know if you have any questions.</p>
    <p>We are pleased to present our new stationery. Every item shares one crisp, streamlined look built on trust and technology. Please let us know if you have any questions.</p>
    <p>We are pleased to present our new stationery. Every item shares one crisp, streamlined look built on trust and technology. Please let us know if you have any questions.</p>
    <p>Best regards,</p>
    <span class="signature" role="img" aria-label="Handwritten signature"></span>
    <p style="margin-top:4px">Henrik Dahlquist<br>CEO</p>
    <div class="faint-square"></div>
  </section>

  <section class="item fax">
    <div class="head">
      <div class="brand md"><span class="mark"></span>Karvelo</div>
      <div class="tiny">Karvelo ApS<br>Birkeslette 218<br>5810 Naestved<br>Denmark</div>
    </div>
    <div class="fax-title">FAX</div>
    <table class="fax-table">
      <tr><td class="lbl">To:</td><td></td><td class="lbl">From:</td><td></td></tr>
      <tr><td class="lbl">Fax:</td><td></td><td class="lbl">Pages:</td><td></td></tr>
      <tr><td class="lbl">Phone:</td><td></td><td class="lbl">Date:</td><td></td></tr>
      <tr><td class="lbl">Re:</td><td></td><td class="lbl">CC:</td><td></td></tr>
    </table>
    <div class="checks"><span>Urgent</span><span>For Review</span><span>Please Comment</span><span>Please Reply</span><span>Please Recycle</span></div>
    <div class="comments">Comments:</div>
    <div class="faint-square"></div>
  </section>

</main>
</body>
</html>
```